Sunny Ladle Kitchen April Competition

The website slider is 990 X 225 pixels to fit in with this website www.sunnyladlekitchen.com.au

We would love a fun, lively, food-oriented slider created for Sunny Ladle Kitchen website. Sunny Ladle Kitchen is a central place where people who love food, cooking for their family and friends, and sharing recipes can hang out. We'd like the sliders to be simple, bright and to entice people to click on the link.

The banner ad needs to feature the Coastal Readers' Monthly cookbooks, and to use a colour scheme that also works with the existing website.

A slider in March was used to promote a similar competition which I will upload as inspiration, along with the image of the cook books to use.

Main text: Add your best mid-week meal recipes to win one of 8 cookbook sets!
Smaller text: The 8 best recipes as chosen by Sunny Ladle Kitchen editors will win.

```html
<!DOCTYPE html>
<html lang="en">
<head>
<meta charset="utf-8">
<title>Sunny Ladle Kitchen April Competition</title>
<link rel="stylesheet" href="https://fonts.googleapis.com/css2?family=Bebas+Neue&family=Oswald:wght@500&family=Patrick+Hand&display=swap">
<style>
  :root {
    --wood-light: #8d8479;
    --wood-mid: #736a60;
    --wood-dark: #564e45;
    --white: #ffffff;
    --teal: #1cb2c3;
    --teal-dark: #14909e;
    --red: #e6283d;
    --book-blue: #27a9dc;
    --book-red: #d8282f;
  }
  * { margin: 0; padding: 0; box-sizing: border-box; }
  html, body { width: 1200px; height: 273px; overflow: hidden; }
  .slider {
    position: relative;
    width: 1200px;
    height: 273px;
    overflow: hidden;
    color: var(--white);
  }
  .wood-backdrop {
    position: absolute;
    inset: 0;
    background:
      linear-gradient(90deg, rgba(0,0,0,0.22) 0%, rgba(0,0,0,0) 30%, rgba(0,0,0,0) 70%, rgba(0,0,0,0.15) 100%),
      linear-gradient(180deg, var(--wood-light) 0%, var(--wood-mid) 55%, var(--wood-dark) 100%);
  }
  .intro {
    position: absolute;
    left: 48px;
    top: 12px;
    font-family: "Patrick Hand", cursive;
    font-size: 30px;
    line-height: 1;
    text-shadow: 0 1px 3px rgba(0,0,0,0.4);
  }
  .headline {
    position: absolute;
    left: 47px;
    top: 42px;
    font-family: "Bebas Neue", sans-serif;
    font-weight: 400;
    font-size: 61px;
    line-height: 1;
    letter-spacing: 0;
    white-space: nowrap;
    text-shadow: 0 2px 4px rgba(0,0,0,0.4);
  }
  .prize-ribbon {
    position: absolute;
    left: 48px;
    top: 107px;
    width: 548px;
    height: 50px;
  }
  .prize-ribbon svg { position: absolute; inset: 0; }
  .prize-ribbon span {
    position: absolute;
    left: 32px;
    top: 0;
    font-family: "Patrick Hand", cursive;
    font-size: 47px;
    line-height: 50px;
    white-space: nowrap;
  }
  .rules {
    position: absolute;
    left: 42px;
    top: 178px;
    font-family: "Oswald", sans-serif;
    font-weight: 500;
    font-size: 16.5px;
    line-height: 20px;
    white-space: nowrap;
    text-shadow: 0 1px 2px rgba(0,0,0,0.5);
  }
  .rules .star { font-size: 14px; margin: 0 6px; }
  .cta-button {
    position: absolute;
    left: 68px;
    top: 208px;
    width: 284px;
    height: 43px;
    background: var(--red);
    display: flex;
    align-items: center;
    justify-content: center;
    gap: 16px;
    font-family: "Bebas Neue", sans-serif;
    font-size: 40px;
    line-height: 1;
    padding-top: 3px;
    letter-spacing: 0.5px;
    color: var(--white);
    text-decoration: none;
    box-shadow: 0 2px 4px rgba(0,0,0,0.35);
  }
  .cta-button svg { width: 16px; height: 18px; margin-top: -3px; }
  .cookbooks {
    position: absolute;
    left: 700px;
    top: 0;
    width: 500px;
    height: 273px;
  }
</style>
</head>
<body>
  <main class="slider">
    <div class="wood-backdrop" role="img" aria-label="Rustic grey wooden tabletop background"></div>

    <p class="intro">add your</p>
    <h1 class="headline">BEST MIDWEEK MEAL RECIPES</h1>

    <div class="prize-ribbon">
      <svg viewBox="0 0 548 50" width="548" height="50" aria-hidden="true">
        <polygon points="0,0 530,0 548,25 530,50 0,50 14,25" fill="var(--teal)"/>
        <polygon points="0,50 14,25 18,50" fill="var(--teal-dark)"/>
      </svg>
      <span>to win 1 of 8 cookbook sets!</span>
    </div>

    <p class="rules"><span class="star">★</span>THE 8 BEST RECIPES AS CHOSEN BY SUNNY LADLE KITCHEN EDITORS WILL WIN.<span class="star">★</span></p>

    <a class="cta-button" href="#">ADD YOURS HERE
      <svg viewBox="0 0 16 18" aria-hidden="true"><polygon points="0,0 16,9 0,18" fill="var(--white)"/></svg>
    </a>

    <svg class="cookbooks" viewBox="0 0 500 273" role="img" aria-label="Two Coastal Readers' Monthly cookbooks lying on the table, one with a blue cover and one with a red cover">
      <path d="M22,62 Q18,50 30,48 L330,26 L336,273 L40,273 Q22,160 22,62 Z" fill="var(--white)"/>
      <polygon points="40,62 324,40 330,273 52,273" fill="var(--book-blue)"/>
      <path d="M170,112 Q166,98 180,96 L500,58 L500,273 L186,273 Q170,190 170,112 Z" fill="var(--white)"/>
      <polygon points="186,112 500,74 500,273 196,273" fill="var(--book-red)"/>
    </svg>
  </main>
</body>
</html>
```